Brell Stone Company Business Cards

Front and Back Business Card - logo and text setup - cool design. I need workable photoshop or illustrator files so I can setup each employee card with design that is created
Updates

Hi everyone, thank you for the great entries. Please no more white and blue cards - there are so many already - black and silver only now please. thanks!

Target Market(s)

Construction Industry - Facility Managers

Industry/Entity Type

Construction

Contact Information for Business Card

I really like contemporary simplistic looks - clean neat....not opposed to seeing some black backrounds

Requirements
Must have
• Logo/website address with design on front only - www.brellstone-example.com (logo attached)
• Back:
• Name/Title/Company Address/Phone/email address
Nice to have
• Cool design
Should not have
• Nothing gimmicky like Fire or Water - since we are a Fire Protection company - it has all been done

```html
<!DOCTYPE html>
<html lang="en">
<head>
<meta charset="utf-8">
<title>Brell Stone Company Business Cards</title>
<link rel="stylesheet" href="https://fonts.googleapis.com/css2?family=Open+Sans:wght@400;600;700&display=swap">
<style>
  :root {
    --page: #1a1a1a;
    --card: #262626;
    --silver: #b9b9b9;
    --silver-bright: #d6d6d6;
    --silver-dim: #8a8a8a;
    --rule: #9a9a9a;
  }
  * { margin: 0; padding: 0; box-sizing: border-box; }
  html, body {
    width: 1200px; height: 900px; overflow: hidden;
    background: var(--page);
    font-family: "Open Sans", Arial, sans-serif;
  }
  .sheet {
    width: 1200px; height: 900px;
    display: flex; flex-direction: column;
    align-items: center; justify-content: center; gap: 40px;
  }
  .card {
    width: 580px; height: 331px;
    background: var(--card);
    position: relative;
    box-shadow: 0 10px 30px rgba(0,0,0,.5);
  }
  /* Front */
  .card-front { display: flex; align-items: center; justify-content: center; }
  .brand {
    display: flex; align-items: baseline; gap: 10px;
    color: var(--silver);
    font-weight: 700;
    margin-top: -20px;
  }
  .brand-name { font-size: 52px; letter-spacing: -1px; }
  .brand-suffix { font-size: 26px; }
  /* Back */
  .card-back { display: flex; align-items: center; padding-left: 70px; }
  .person { width: 200px; text-align: left; margin-top: 70px; }
  .person-name {
    color: var(--silver-bright);
    font-size: 19px; font-weight: 600; letter-spacing: .5px;
    text-transform: uppercase;
  }
  .person-title { color: var(--silver-dim); font-size: 13px; margin-top: 2px; }
  .divider {
    width: 1px; height: 120px; background: var(--rule);
    margin: 0 18px 0 20px;
  }
  .contact { color: var(--silver); font-size: 13px; line-height: 1.55; }
  .contact-address { margin-bottom: 6px; }
  .contact-line { display: flex; align-items: center; gap: 7px; }
  .contact-icon { width: 11px; height: 11px; flex: none; }
</style>
</head>
<body>
<main class="sheet">
  <section class="card card-front" aria-label="Card front">
    <div class="brand">
      <span class="brand-name">brellstone</span>
      <span class="brand-suffix">inc.</span>
    </div>
  </section>

  <section class="card card-back" aria-label="Card back">
    <div class="person">
      <p class="person-name">Dale Whitcombe</p>
      <p class="person-title">President</p>
    </div>
    <div class="divider"></div>
    <div class="contact">
      <p class="contact-address">48 Meridian Way<br>Harlow Point, NY 10990</p>
      <p class="contact-line">
        <svg class="contact-icon" viewBox="0 0 12 12" aria-hidden="true"><path fill="#b9b9b9" d="M2.5 1l2 2-1 1.5c.6 1.4 1.6 2.4 3 3L8 6.5l2 2-1.2 1.8C5 10 2 7 1.7 3.2z"/></svg>
        (555) 014-2870
      </p>
      <p class="contact-line">
        <svg class="contact-icon" viewBox="0 0 12 12" aria-hidden="true"><rect x="1" y="2.5" width="10" height="7" fill="#b9b9b9"/><path d="M1 2.5l5 4 5-4" fill="none" stroke="#262626" stroke-width="1"/></svg>
        info@brellstone-example.com
      </p>
      <p class="contact-line">
        <svg class="contact-icon" viewBox="0 0 12 12" aria-hidden="true"><circle cx="6" cy="6" r="5" fill="none" stroke="#b9b9b9" stroke-width="1.2"/><path d="M1 6h10M6 1c-2 2.5-2 7.5 0 10M6 1c2 2.5 2 7.5 0 10" fill="none" stroke="#b9b9b9" stroke-width=".9"/></svg>
        www.brellstone-example.com
      </p>
    </div>
  </section>
</main>
</body>
</html>
```